A Modern & Sleek "Coming Soon" Page for an A.I Recruiting App

For the “Coming Soon” website, a simple background with no people in it. I've attached an A.I image of what the page should generally look like.

- A single mobile phone as the main focus where the user actually clicks on the, “notify me” button (after entering their email address).
- In the background where the pillars/columns are seen in the example, should be subtle pad locks that are in their opened position with a key inside the lock. I've attached images to try to illustrate this idea, but they are far away in style from what I'm looking for.

SLOGAN: Unlocking the power of meaningful connections
LOGO/TITLE: Should be the name as shown in image with only the name "KelvoLink" on it
COLORS: Purplish/blue hues. Should not be too feminine
NOTE: The user should only click once when signing up/entering their email.

Product: A recruiting platform that matches employers/employees with A.I. and prioritizing cultural fit/values system before skills. The industry we are tackling first is the caregiving industry (nannies, tutors, elderly). All users will be background screened and that info lives on the blockchain. All users will have the option to review and be reviewed/rated.

```html
<!DOCTYPE html>
<html lang="en">
<head>
<meta charset="UTF-8">
<title>KelvoLink – Coming Soon</title>
<link rel="stylesheet" href="https://fonts.googleapis.com/css2?family=Montserrat:wght@200;500;600&family=Roboto:wght@400&display=swap">
<style>
  :root {
    --night: #110d2c;
    --deep-navy: #0b1030;
    --violet-glow: #3a1f78;
    --teal-glow: #1f6f86;
    --teal-soft: #2a8fa8;
    --screen-light: #7cc3cf;
    --screen-deep: #1c8aa8;
    --phone-edge: #0c1a2a;
    --white: #ffffff;
    --field-text: #8b8b95;
    --button-purple: #4b2699;
  }

  * { box-sizing: border-box; margin: 0; padding: 0; }

  html, body {
    width: 1200px;
    height: 667px;
    overflow: hidden;
    background: var(--night);
  }

  .coming-soon {
    position: relative;
    width: 1200px;
    height: 667px;
    overflow: hidden;
    background:
      radial-gradient(ellipse 520px 260px at 560px 600px, rgba(42, 143, 168, 0.55), transparent 70%),
      radial-gradient(ellipse 420px 300px at 60px 420px, rgba(31, 111, 134, 0.55), transparent 70%),
      radial-gradient(ellipse 500px 360px at 1150px 120px, rgba(90, 40, 160, 0.55), transparent 70%),
      radial-gradient(ellipse 600px 300px at 1100px 560px, rgba(58, 31, 120, 0.5), transparent 70%),
      linear-gradient(135deg, var(--deep-navy) 0%, var(--night) 55%, #1a0f3a 100%);
  }

  .lock-backdrop {
    position: absolute;
    left: 400px;
    top: 110px;
    width: 720px;
    height: 500px;
    border-radius: 50%;
    background: radial-gradient(ellipse at center, rgba(120, 110, 170, 0.14), transparent 70%);
  }

  .phone-visual {
    position: absolute;
    left: 108px;
    top: 84px;
    width: 320px;
    height: 545px;
    border-radius: 46px;
    border: 9px solid var(--phone-edge);
    background: linear-gradient(170deg, var(--screen-light) 0%, #55aebf 45%, var(--screen-deep) 100%);
    transform: rotate(-3deg) skewY(2deg);
    box-shadow: 0 30px 60px rgba(0, 0, 0, 0.5);
  }

  .hero {
    position: absolute;
    left: 440px;
    top: 190px;
    width: 690px;
    text-align: center;
  }

  .brand-name {
    font-family: "Montserrat", sans-serif;
    font-weight: 200;
    font-size: 80px;
    line-height: 1;
    letter-spacing: 8px;
    text-transform: uppercase;
    color: var(--white);
  }

  .slogan {
    margin-top: 52px;
    font-family: "Roboto", sans-serif;
    font-weight: 400;
    font-size: 25px;
    color: var(--white);
  }

  .signup {
    position: absolute;
    left: 519px;
    top: 392px;
    display: flex;
    gap: 19px;
  }

  .signup-email {
    width: 315px;
    height: 64px;
    border: none;
    border-radius: 32px;
    background: var(--white);
    padding: 0 20px;
    font-family: "Montserrat", sans-serif;
    font-weight: 500;
    font-size: 16px;
    letter-spacing: 0.5px;
    color: #333;
    outline: none;
  }

  .signup-email::placeholder {
    color: var(--field-text);
    text-transform: uppercase;
  }

  .signup-button {
    width: 187px;
    height: 64px;
    border: none;
    border-radius: 32px;
    background: var(--button-purple);
    color: var(--white);
    font-family: "Montserrat", sans-serif;
    font-weight: 600;
    font-size: 18px;
    letter-spacing: 0.5px;
    text-transform: uppercase;
    cursor: pointer;
  }
</style>
</head>
<body>
  <main class="coming-soon">
    <div class="lock-backdrop" role="img" aria-label="Faint open padlock with circuit lines and binary digits in the background"></div>

    <div class="phone-visual" role="img" aria-label="Smartphone showing the KelvoLink notify-me sign-up screen"></div>

    <header class="hero">
      <h1 class="brand-name">KelvoLink</h1>
      <p class="slogan">Unlocking the Power Of Meaningful Connections</p>
    </header>

    <div class="signup">
      <input class="signup-email" type="email" placeholder="Enter email here" aria-label="Email address">
      <button class="signup-button" type="button">Sign me up</button>
    </div>
  </main>
</body>
</html>
```